A landing page for an exclusive club VELKARDO

We need a fresh, stylish and luxury design for a landing page of an international private club called VELKARDO.

After receiving your first drafts, let me briefly emphasize some important points:
1) Top picture: I would like to see here some good looking intelligent people (not dancing teenagers or smiling couple – because it’s not a pure dating website)
2) Member’s section: the main message of this slide is to communicate the idea of EXCLUSIVITY - the club has exclusive audience (well-educated, intellectual, financially successful people from world-leading universities and well-known companies). I do not want to reveal real members’ profiles on this slide (it’s allowed only in the review section)
3) Event section should not have real future events, just describe event categories.
4) Technology section should communicate the idea of sending REAL presents (a drink or flowers) to a girl via the app. (maybe by using some dynamic elements during the scrolling)
5) Review section – please make it individual design, not a standard one. Please add company’s names and job titles to reviewers.
6) Event section: we will not post actual events, rather some event categories with large attractive pictures.
7) Technical note: We do not have “register” button – people can log in or register only via QN – it’s one button
Let me know if you have any questions. Thank you for participating!

Kind regards,
Teodor Vashkin

Reason: Dear designers, I have to extend the deadline as I did not receive any 5* designs so far. I would like to get a unique design - not a combination of standard blocks for landing pages. I understand the task is difficult, so I decided to give you more time to prepare well-though and original piece of art. Please use the text from the brief and add your ideas. The 3 main messages to communicate are: 1) Member’s section: the main message of this slide is to communicate the idea of EXCLUSIVITY - the club has exclusive audience (well-educated, intellectual, successful people from world-leading universities and well-known companies). I do not want to reveal real members’ profiles on this slide (it’s allowed only in the review section). 2) Event section: the club runs lots of invitation-only events in most exclusive venues. We will not post actual events, but rather some event categories with large attractive pictures and short descriptions. 3) Technology section should communicate the idea of sending REAL presents (a drink or flowers) to a girl via the app. If you can show it by using some dynamic elements during the scrolling it's fantastic! Good luck! I look forward for your creative ideas and art! Kind regards, Teodor Vashkin

Target Market(s)

Alumni of top universities, middle- and top-level managers of large companies, financial professionals (investment bankers), successful entrepreneurs, recognized creative class (fashion designers, models).

Industry/Entity Type

Club

Coding

Coded - Design and coding required

Number of Pages Required

2 page

Font styles to use
Serif
Sans Serif
Other font styles liked:
• Lato, Oswald, Raleway

Requirements
Must have
• Adaptive design (desktop & mobile)
• Elegant and luxury design
• Structure according to the brief
Nice to have
• Dynamic elements/Layers on the landing page
Should not have
• Trivial stock photos.

```html
<!DOCTYPE html>
<html lang="en">
<head>
<meta charset="utf-8">
<title>VELKARDO — Social Discovery Club</title>
<link href="https://fonts.googleapis.com/css2?family=Arimo:wght@400;700&family=Source+Sans+3:wght@400;600&display=swap" rel="stylesheet">
<style>
:root{
  --ink:#2e3142;
  --ink-deep:#272a39;
  --card:#393c4f;
  --band:#4a5494;
  --band-light:#525da0;
  --band-dark:#434d8a;
  --white:#ffffff;
  --soft:#c9cbd8;
  --muted:#8e91a6;
  --rule:rgba(255,255,255,.22);
  --pie-purple:#7b3aa6;
  --pie-grey:#8a8a8e;
  --pie-blue:#1e6fc0;
}
*{margin:0;padding:0;box-sizing:border-box}
html,body{width:1200px;height:4091px;overflow:hidden}
body{position:relative;background:var(--ink);color:var(--white);font-family:"Source Sans 3",Arial,sans-serif}
.abs{position:absolute}
.hero{left:0;top:0;width:1200px;height:520px;background:linear-gradient(180deg,#3f4458 0%,#4d5368 40%,#565d72 65%,#3d4257 100%)}
.nav-strip{left:0;top:0;width:1200px;height:78px;background:rgba(40,43,58,.35)}
.nav{top:30px;left:0;width:1200px;display:flex;justify-content:center;gap:34px;font-family:"Arimo",Arial,sans-serif;font-weight:700;font-size:14px}
.nav a{color:var(--white);text-decoration:none}
.brand-mark{left:562px;top:120px;width:76px;height:76px;border:3px solid var(--white);border-radius:50%}
.brand-name{top:218px;left:0;width:1200px;text-align:center;font-family:"Arimo",Arial,sans-serif;font-size:24px;letter-spacing:14px;padding-left:14px}
.brand-tag{top:280px;left:0;width:1200px;text-align:center;font-family:"Arimo",Arial,sans-serif;font-size:22px;color:var(--soft)}
.bands{left:0;top:380px}
.topic{width:586px}
.topic h2{font-family:"Arimo",Arial,sans-serif;font-size:30px;font-weight:400;padding-bottom:16px;border-bottom:1px solid var(--rule)}
.topic p{font-size:15px;line-height:1.6;color:var(--soft);margin-top:12px}
.topic.right{text-align:right}
.more{display:flex;align-items:center;gap:16px;margin-top:22px;font-family:"Arimo",Arial,sans-serif;font-weight:700;font-size:12px;letter-spacing:1px}
.topic.right .more{justify-content:flex-end}
.more i{width:30px;height:30px;border:1px solid var(--rule);border-radius:50%;display:flex;align-items:center;justify-content:center;font-style:normal}
.pie{position:absolute}
.section-title{font-family:"Arimo",Arial,sans-serif;font-size:30px;font-weight:400}
.lead{font-size:15px;line-height:1.6;color:var(--soft);width:864px}
.card{width:410px;height:456px;background:var(--card)}
.card .photo{height:237px;position:relative;background:linear-gradient(160deg,#7f8a8c,#4f5658 60%,#3a3f44)}
.card .frame{position:absolute;left:130px;top:43px;width:150px;height:150px;background:var(--white);display:flex;align-items:center;justify-content:center}
.card .frame span{width:130px;height:130px;border-radius:50%;background:radial-gradient(circle at 50% 45%,#8a6a58,#3a2c28 75%)}
.card h3{font-family:"Arimo",Arial,sans-serif;font-size:15px;margin:32px 30px 0;padding-bottom:16px;border-bottom:1px solid var(--rule)}
.card p{font-size:14px;line-height:1.6;color:var(--soft);margin:14px 30px 0}
.card .more{margin:24px 30px 0}
.btn{border:1px solid var(--rule);font-family:"Arimo",Arial,sans-serif;font-weight:700;font-size:12px;letter-spacing:1px;display:flex;align-items:center;justify-content:center}
.contact-bg{left:0;top:3130px;width:1200px;height:961px;background:linear-gradient(180deg,#3a3e51 0%,#424659 22%,#34374a 60%,var(--ink-deep) 100%);clip-path:polygon(0 100px,1200px 0,1200px 961px,0 961px)}
.label{font-family:"Arimo",Arial,sans-serif;font-weight:700;font-size:12px;letter-spacing:1px}
.field{border:1px solid var(--rule);background:rgba(255,255,255,.04);width:409px}
.info{left:641px;display:flex;align-items:flex-start;gap:12px;font-size:14px;line-height:1.55;color:var(--soft)}
.info i{width:23px;height:23px;border-radius:50%;background:rgba(255,255,255,.14);flex:none;display:flex;align-items:center;justify-content:center}
.footer-rule{left:169px;top:3960px;width:862px;height:1px;background:var(--rule)}
.copy{left:169px;top:4000px;font-size:12px;color:var(--muted)}
</style>
</head>
<body>

<header>
  <div class="abs hero" role="img" aria-label="Misty mountain range at dusk in cool blue-grey tones"></div>
  <div class="abs nav-strip"></div>
  <nav class="abs nav"><a href="#">Home</a><a href="#">About Us</a><a href="#">Services</a><a href="#">Portfolio</a><a href="#">Contact Us</a></nav>
  <div class="abs brand-mark"></div>
  <div class="abs brand-name">VELKARDO</div>
  <div class="abs brand-tag">SOCIAL DISCOVERY CLUB</div>
</header>

<svg class="abs bands" width="1200" height="1420" viewBox="0 380 1200 1420" aria-hidden="true">
  <polygon points="0,491 1200,395 1200,1786 0,1677" fill="var(--band)"/>
  <polygon points="0,491 1200,395 1200,700 0,820" fill="var(--band-light)"/>
  <polygon points="0,1060 1200,1180 1200,1786 0,1677" fill="var(--band-dark)"/>
  <polygon points="0,1360 1200,1300 1200,1786 0,1677" fill="#3f4885"/>
</svg>

<section class="abs topic right" style="left:169px;top:552px">
  <h2>EDUCATION</h2>
  <p>Lorem ipsum dolor sit amet, etiam lorem adipiscing elit. Cras turpis ante, nullam sit amet turpis non, sollicitudin posuere urna. Mauris id tellus arcu. Nunc vehicula id nulla dignissim dapibus. Nullam ultrices, neque et faucibus viverra, ex nulla cursus.</p>
  <div class="more"><i>›</i>LEARN MORE</div>
</section>
<svg class="pie" style="left:791px;top:537px" width="246" height="246" viewBox="0 0 246 246" role="img" aria-label="Education chart">
  <g stroke="#fff" stroke-width="3">
    <path d="M123 123 L123 3 A120 120 0 0 1 239 92 Z" fill="var(--pie-grey)"/>
    <path d="M123 123 L239 92 A120 120 0 0 1 123 243 Z" fill="var(--pie-blue)"/>
    <path d="M123 123 L123 243 A120 120 0 0 1 123 3 Z" fill="var(--pie-purple)"/>
  </g>
</svg>

<section class="abs topic" style="left:450px;top:980px">
  <h2>FAMILY</h2>
  <p>Lorem ipsum dolor sit amet, etiam lorem adipiscing elit. Cras turpis ante, nullam sit amet turpis non, sollicitudin posuere urna. Mauris id tellus arcu. Nunc vehicula id nulla dignissim dapibus. Nullam ultrices, neque et faucibus viverra, ex nulla cursus.</p>
  <div class="more"><i>›</i>LEARN MORE</div>
</section>
<svg class="pie" style="left:158px;top:963px" width="262" height="262" viewBox="0 0 262 262" role="img" aria-label="Family chart">
  <g stroke="#fff" stroke-width="3">
    <path d="M131 131 L7 98 A128 128 0 0 1 131 3 Z" fill="var(--pie-grey)"/>
    <path d="M131 131 L131 3 A128 128 0 1 1 7 98 Z" fill="var(--pie-blue)"/>
  </g>
</svg>

<section class="abs topic right" style="left:169px;top:1411px">
  <h2>GENDER &amp; AGE</h2>
  <p>Lorem ipsum dolor sit amet, etiam lorem adipiscing elit. Cras turpis ante, nullam sit amet turpis non, sollicitudin posuere urna. Mauris id tellus arcu. Nunc vehicula id nulla dignissim dapibus. Nullam ultrices, neque et faucibus viverra, ex nulla cursus.</p>
  <div class="more"><i>›</i>LEARN MORE</div>
</section>
<svg class="pie" style="left:791px;top:1393px" width="246" height="246" viewBox="0 0 246 246" role="img" aria-label="Gender and age chart">
  <g stroke="#fff" stroke-width="3">
    <path d="M123 123 L123 3 A120 120 0 0 1 183 227 Z" fill="var(--pie-grey)"/>
    <path d="M123 123 L183 227 A120 120 0 0 1 54 221 Z" fill="var(--pie-blue)"/>
    <path d="M123 123 L54 221 A120 120 0 0 1 123 3 Z" fill="var(--pie-purple)"/>
  </g>
</svg>

<h2 class="abs section-title" style="left:169px;top:1834px">VELKARDO CLUB RELATIONSHIP</h2>
<p class="abs lead" style="left:169px;top:1906px">Cras mattis ante fermentum, malesuada neque vitae, eleifend erat. Phasellus non pulvinar erat. Fusce tincidunt, nisl eget mattis egestas, purus ipsum consequat orci, sit amet lobortis lorem lacus in tellus. Sed ac elementum arcu. Quisque placerat auctor laoreet.</p>

<article class="abs card" style="left:169px;top:2018px">
  <div class="photo" role="img" aria-label="Road through a mountain valley with a round inset of club members at a meetup"><div class="frame"><span></span></div></div>
  <h3>ALUMNI MEETUPS</h3>
  <p>Lorem ipsum dolor sit amet, consectetur adipiscing vehicula id nulla dignissim dapibus ultrices.</p>
  <div class="more"><i>›</i>LEARN MORE</div>
</article>
<article class="abs card" style="left:624px;top:2018px">
  <div class="photo" style="background:linear-gradient(160deg,#6f7a66,#4a5446 60%,#353b33)" role="img" aria-label="Wooden cabin among trees with a round inset of guests at a quiz night"><div class="frame"><span></span></div></div>
  <h3>QUIZ NIGHTS</h3>
  <p>Lorem ipsum dolor sit amet, consectetur adipiscing vehicula id nulla dignissim dapibus ultrices.</p>
  <div class="more"><i>›</i>LEARN MORE</div>
</article>
<article class="abs card" style="left:169px;top:2522px">
  <div class="photo" style="background:linear-gradient(170deg,#9a9a90,#5d6260 55%,#3c4144)" role="img" aria-label="Hillside view over a town with a round inset of guests at a private viewing"><div class="frame"><span></span></div></div>
  <h3>PRIVATE VIEWINGS</h3>
  <p>Lorem ipsum dolor sit amet, consectetur adipiscing vehicula id nulla dignissim dapibus ultrices.</p>
  <div class="more"><i>›</i>LEARN MORE</div>
</article>
<article class="abs card" style="left:624px;top:2522px">
  <div class="photo" style="background:linear-gradient(150deg,#8c90a6,#5a5e72 55%,#3b3e4e)" role="img" aria-label="Modern building facade with a round inset of guests at a networking lunch"><div class="frame"><span></span></div></div>
  <h3>NETWORKING LUNCHES</h3>
  <p>Lorem ipsum dolor sit amet, consectetur adipiscing vehicula id nulla dignissim dapibus ultrices.</p>
  <div class="more"><i>›</i>LEARN MORE</div>
</article>

<div class="abs btn" style="left:169px;top:3032px;width:150px;height:46px">BROWSE ALL</div>

<div class="abs contact-bg" role="img" aria-label="Faint layered mountain silhouettes in slate tones"></div>

<h2 class="abs section-title" style="left:169px;top:3308px">GET IN TOUCH</h2>
<p class="abs lead" style="left:169px;top:3384px">Cras mattis ante fermentum, malesuada neque vitae, eleifend erat. Phasellus non pulvinar erat. Fusce tincidunt, nisl eget mattis egestas, purus ipsum consequat orci, sit amet lobortis lorem lacus in tellus. Sed ac elementum arcu. Quisque placerat auctor laoreet.</p>

<div class="abs label" style="left:169px;top:3464px">NAME</div>
<div class="abs field" style="left:169px;top:3492px;height:44px"></div>
<div class="abs label" style="left:169px;top:3552px">EMAIL</div>
<div class="abs field" style="left:169px;top:3578px;height:44px"></div>
<div class="abs label" style="left:169px;top:3638px">MESSAGE</div>
<div class="abs field" style="left:169px;top:3665px;height:126px"></div>
<div class="abs btn" style="left:169px;top:3826px;width:170px;height:46px">SEND MESSAGE</div>

<div class="abs info" style="top:3462px"><i><svg width="11" height="11" viewBox="0 0 12 12"><path d="M1 6 L6 1 L11 6 V11 H1 Z" fill="#fff"/></svg></i><span>Norvale Inc<br>48 Harrow Lane Suite #210<br>Calder, TN 00000-0000</span></div>
<div class="abs info" style="top:3580px"><i><svg width="11" height="11" viewBox="0 0 12 12"><path d="M2 1 L4.5 1 L5.5 4 L4 5 Q5 7.5 7 8 L8 6.5 L11 7.5 L11 10 Q6 11.5 1 3 Z" fill="#fff"/></svg></i><span>(555) 014-2276</span></div>
<div class="abs info" style="top:3646px"><i><svg width="11" height="9" viewBox="0 0 12 10"><rect x="0.5" y="0.5" width="11" height="9" fill="none" stroke="#fff"/><path d="M0.5 0.5 L6 5.5 L11.5 0.5" fill="none" stroke="#fff"/></svg></i><span>hello@norvale.tld</span></div>
<div class="abs info" style="top:3712px"><i></i><span>chirp.norvale.tld</span></div>
<div class="abs info" style="top:3777px"><i></i><span>circle.norvale.tld</span></div>
<div class="abs info" style="top:3842px"><i></i><span>frames.norvale.tld</span></div>

<div class="abs footer-rule"></div>
<p class="abs copy">© Norvale Inc. All rights reserved.</p>

</body>
</html>
```